Layout, Design eines Produktfolders
Zielgruppe
Potentielle Kooperationspartner aus dem Bereich Sensorhersteller, Kunden, Potentielle Vertriebspartner aus verwandten Branchen
Aufgabenstellung
Ergebnis soll eine Broschüre im Querformat A5, 6-seitig, aufklappbar sein.
Ein erster Designentwurf wurde erstellt, dieser soll modifiziert und neu umgesetzt werden.
Wenn möglich soll der Erstentwurf im Ergebnis erkennbar bzw. das Ergebnis am ersten Entwurf angelehnt sein.

```html
<!DOCTYPE html>
<html lang="en">
<head>
<meta charset="utf-8">
<title>glacerio – Product Sheet</title>
<link href="https://fonts.googleapis.com/css2?family=Arimo:wght@400;700&display=swap" rel="stylesheet">
<style>
  :root {
    --ink: #1a1a1a;
    --brand-blue: #1d5e97;
    --bullet-blue: #1b5b93;
    --panel-top: #f1f2f4;
    --panel-mid: #e3e5e8;
    --panel-bottom: #fafafb;
    --rule: #c4c6ca;
    --page: #ffffff;
  }
  html, body {
    margin: 0;
    padding: 0;
    overflow: hidden;
    background: var(--page);
  }
  .sheet {
    position: relative;
    width: 1200px;
    height: 845px;
    overflow: hidden;
    background: var(--page);
    font-family: "Arimo", Arial, sans-serif;
    color: var(--ink);
  }
  .photo-strip {
    position: absolute;
    top: 0;
    left: 0;
    width: 1200px;
    height: 150px;
    display: flex;
  }
  .photo-strip .photo { flex: 1 1 0; height: 100%; }
  .photo--road { background: linear-gradient(180deg, #5d8fc9 0%, #bcd3ea 40%, #4f8a3a 62%, #6b6e72 80%, #4a4c50 100%); }
  .photo--berries { background: linear-gradient(135deg, #c8202c 0%, #3f5fa8 45%, #2b3270 70%, #1a1a2a 100%); }
  .photo--fish { background: linear-gradient(180deg, #7c8a86 0%, #c2ccc6 45%, #5d6b68 100%); }
  .photo--vials { background: linear-gradient(160deg, #f3f3f0 0%, #e8d16a 40%, #ffffff 60%, #2f6bc0 100%); }
  .photo--ampoules { background: linear-gradient(135deg, #2a2742 0%, #7b5a8e 40%, #c7c9d6 65%, #2f2c4a 100%); }
  .photo--runway { background: linear-gradient(180deg, #3b4756 0%, #a7b2bd 40%, #6d8a45 55%, #5a5e62 72%, #3a3d41 100%); }

  .content-panel {
    position: absolute;
    top: 150px;
    left: 0;
    width: 1200px;
    height: 567px;
    background: linear-gradient(180deg, var(--panel-top) 0%, var(--panel-mid) 20%, #eceef0 60%, var(--panel-bottom) 100%);
    border-bottom: 3px solid var(--rule);
  }
  .product-name {
    position: absolute;
    left: 12px;
    top: 22px;
    margin: 0;
    font-size: 40px;
    font-weight: 700;
    color: var(--brand-blue);
    letter-spacing: 1px;
  }
  .feature-list {
    list-style: none;
    margin: 0;
    padding: 0;
  }
  .feature {
    position: absolute;
    left: 237px;
    width: 940px;
    display: flex;
    align-items: flex-start;
  }
  .feature-dot {
    flex: none;
    width: 33px;
    height: 33px;
    border-radius: 50%;
    background: radial-gradient(circle at 35% 30%, #4d8cc4 0%, var(--bullet-blue) 55%, #0f3d68 100%);
    margin-right: 23px;
    margin-top: -3px;
  }
  .feature-text {
    font-size: 24px;
    line-height: 28px;
    margin: 0;
    white-space: nowrap;
  }
</style>
</head>
<body>
<div class="sheet">
  <div class="photo-strip">
    <div class="photo photo--road" role="img" aria-label="Truck on a country road under a blue sky"></div>
    <div class="photo photo--berries" role="img" aria-label="Fresh strawberries, blueberries and blackberries"></div>
    <div class="photo photo--fish" role="img" aria-label="Fresh fish packed together"></div>
    <div class="photo photo--vials" role="img" aria-label="Laboratory vials and bottles"></div>
    <div class="photo photo--ampoules" role="img" aria-label="Pharmaceutical glass ampoules"></div>
    <div class="photo photo--runway" role="img" aria-label="Airplane taking off from a runway"></div>
  </div>

  <section class="content-panel">
    <h1 class="product-name">glacerio</h1>
    <ul class="feature-list">
      <li class="feature" style="top:92px"><span class="feature-dot"></span><p class="feature-text">is a revolutionary sensor-solution for wireless cold-chain monitoring in foodstuff<br>and pharmacy transportation.</p></li>
      <li class="feature" style="top:186px"><span class="feature-dot"></span><p class="feature-text">is characterized by high reliability, precision and easy handling.</p></li>
      <li class="feature" style="top:252px"><span class="feature-dot"></span><p class="feature-text">is grounded on a concept that has been used in common electronic article<br>surveillance systems for years.</p></li>
      <li class="feature" style="top:355px"><span class="feature-dot"></span><p class="feature-text">does not need any energy supply.</p></li>
      <li class="feature" style="top:428px"><span class="feature-dot"></span><p class="feature-text">can be detected secured from up to two meters distance.</p></li>
      <li class="feature" style="top:498px"><span class="feature-dot"></span><p class="feature-text">guarantees a precise temperature control at a reasonable price</p></li>
    </ul>
  </section>
</div>
</body>
</html>
```